Real Estate and Entertainment Fund - Capital Raise

We need a Power Point presentation to raise capital for 2 funds. One is focused on Real Estate and the other one in Entertainment. We'd like for it to be professional with lots of pictures and graphs. The color palette should match the Fund Logo.
We provide the basic content of the presentation in the document attached
Updates

Target Market(s)

Milennial Investors

```html
<!DOCTYPE html>
<html lang="en">
<head>
<meta charset="utf-8">
<title>Royal Crane – Pitch Presentation</title>
<link rel="stylesheet" href="https://fonts.googleapis.com/css2?family=Roboto+Condensed:wght@400;700&family=Roboto:wght@400;700&display=swap">
<style>
:root{
  --page:#e7e7e7;
  --white:#ffffff;
  --coral:#f0655f;
  --red:#e6312b;
  --deep:#9c1212;
  --darkest:#5a0b0b;
  --ink:#222222;
  --grey:#8a8a8a;
  --light:#ececec;
}
*{box-sizing:border-box;margin:0;padding:0}
html,body{width:1200px;height:4203px;overflow:hidden}
body{background:var(--page);font-family:'Roboto',sans-serif;color:var(--ink);position:relative}
.slide{position:absolute;width:556px;height:312px;background:var(--white);box-shadow:0 1px 5px rgba(0,0,0,.28);overflow:hidden}
.col-l{left:24px}.col-r{left:606px}
.abs{position:absolute}
.s-title{position:absolute;top:22px;left:0;right:0;text-align:center;font-family:'Roboto Condensed',sans-serif;font-size:17px;color:var(--coral);text-transform:uppercase;letter-spacing:.2px}
.s-title.left{left:30px;text-align:left}
.s-title.plain{text-transform:none}
.s-sub{position:absolute;top:44px;left:0;right:0;text-align:center;font-size:5px;color:var(--grey);letter-spacing:.3px;text-transform:uppercase}
.brand{position:absolute;top:14px;right:16px;display:flex;align-items:center;gap:4px;font-family:'Roboto Condensed',sans-serif;font-weight:700;font-size:7px;color:var(--red);letter-spacing:.6px}
.brand i{display:block;width:12px;height:12px;background:var(--red)}
.foot{position:absolute;bottom:7px;left:22px;font-size:4.5px;color:var(--grey)}
.foot b{color:var(--coral);font-weight:400}
.para{font-size:6.5px;line-height:1.45;color:#444}
.photo{position:absolute;background:linear-gradient(135deg,#dcdcdc,#c9c9c9)}
.art{position:absolute;background:linear-gradient(160deg,#f4827c,var(--coral) 60%,#e9544d)}
.art.muted{background:linear-gradient(160deg,#b87a76,#8f5552)}
.cap{position:absolute;font-size:5px;color:#fff}
.hero{position:absolute;left:60px;top:21px;width:1070px;height:601px;background:var(--white);box-shadow:0 2px 8px rgba(0,0,0,.25);overflow:hidden}
.hero h1{position:absolute;left:617px;top:320px;font-family:'Roboto Condensed',sans-serif;font-weight:700;font-size:54px;line-height:.98;color:#111;letter-spacing:.5px}
.hero h1 span{color:var(--coral);display:block}
.hero .rule{position:absolute;left:620px;top:452px;width:360px;height:1px;background:#ddd}
.hero .tag{position:absolute;left:620px;top:464px;font-size:10px;letter-spacing:5px;color:#666}
table{border-collapse:collapse;width:100%}
.t-brand td,.t-brand th{border:.5px solid #999;font-size:5.4px;text-align:center;padding:2px 2px;height:18px}
.t-brand th{background:var(--red);color:#fff;font-weight:700}
.t-brand td.nm{background:var(--red);color:#fff;font-weight:700}
.t-fin td,.t-fin th{font-size:5.6px;padding:1.6px 4px;text-align:center;border-bottom:.5px solid #ddd}
.t-fin th{background:var(--red);color:#fff;font-weight:400}
.t-fin td:first-child{text-align:left}
.t-fin tr.net td{background:#bfbfbf;font-size:6.5px;color:#222}
.ticks{position:absolute;display:flex;flex-direction:column;gap:5px}
.tick{display:flex;gap:6px;align-items:flex-start}
.tick .dot{width:14px;height:14px;border-radius:50%;background:var(--red);flex:none;display:flex;align-items:center;justify-content:center}
.tick h4{font-family:'Roboto Condensed',sans-serif;font-size:6.5px;color:var(--red);font-weight:700}
.tick p{font-size:4.8px;color:#888;line-height:1.35;width:170px}
.benefit{position:absolute;left:62px;width:435px;height:52px;border:1px solid var(--coral);display:flex;align-items:center;gap:14px;padding:0 12px}
.benefit h4{font-family:'Roboto Condensed',sans-serif;font-weight:400;font-size:9px;color:var(--red)}
.benefit p{font-size:5px;color:#555;margin-top:3px}
.circ{position:absolute;display:flex;align-items:center;gap:10px}
.circ i{display:block;width:44px;height:44px;border-radius:50%}
.circ h4{font-family:'Roboto Condensed',sans-serif;font-size:9px;font-weight:400}
.circ p{font-size:5px;color:#777;width:110px;line-height:1.35}
.tl-year{position:absolute;font-family:'Roboto Condensed',sans-serif;font-weight:700;font-size:9px;transform:translateX(-50%)}
.tl-text{position:absolute;width:90px;transform:translateX(-50%);text-align:center;font-size:5px;color:#666;line-height:1.3}
.tl-text b{display:block;color:var(--coral);font-size:6px}
.tl-text.alt b{color:#3a7bd5}
.tl-node{position:absolute;width:26px;height:26px;border-radius:50%;background:var(--red);border:2px solid #fff;box-shadow:0 0 0 1.5px var(--red);transform:translate(-50%,-50%);display:flex;align-items:center;justify-content:center}
.tl-stem{position:absolute;width:1.5px;background:var(--red)}
.call{position:absolute;color:#fff;padding:5px 9px}
.call.red{background:var(--red)}
.call.gray{background:#8f8f8f}
.call h4{font-family:'Roboto',sans-serif;font-weight:400;font-size:11px}
.call p{font-size:5px;line-height:1.35;margin-top:3px}
.call small{display:block;font-size:4.5px;opacity:.8}
.date{position:absolute;text-align:right;width:56px;font-size:5px;color:#666;line-height:1}
.date b{display:block;font-size:14px;color:#222;font-weight:400;margin-top:1px}
.vnode{position:absolute;width:16px;height:16px;border-radius:50%;background:#777;border:2px solid #ddd;transform:translate(-50%,-50%)}
</style>
</head>
<body>

<section class="hero">
  <svg class="abs" style="left:0;top:0" width="720" height="601" viewBox="0 0 720 601">
    <defs>
      <linearGradient id="heroFill" x1="0" y1="1" x2="1" y2="0">
        <stop offset="0" stop-color="#5b6fc4"/>
        <stop offset=".35" stop-color="#f0655f"/>
        <stop offset="1" stop-color="#f6948f"/>
      </linearGradient>
    </defs>
    <line x1="0" y1="440" x2="710" y2="-10" stroke="#f0655f" stroke-width="1"/>
    <line x1="110" y1="610" x2="720" y2="190" stroke="#f0655f" stroke-width="1"/>
    <polygon role="img" aria-label="Striped crane illustration in coral and blue" points="70,430 430,40 650,40 300,560 120,560" fill="url(#heroFill)"/>
  </svg>
  <h1>YOUR PITCH<span>PRESENTATION</span></h1>
  <div class="rule"></div>
  <div class="tag">ROYAL CRANE &nbsp; BUSINESS &nbsp; PRESENTATION</div>
</section>

<!-- ROW 1 -->
<section class="slide col-l" style="top:642px">
  <div class="s-title plain left" style="top:24px;font-size:15px;color:var(--red)">2 investment funds in one family for different kind of investors</div>
  <div class="abs" style="left:236px;top:48px;width:70px;height:1.5px;background:var(--red)"></div>
  <div class="art" style="left:16px;top:84px;width:222px;height:90px" role="img" aria-label="Crane fund artwork on coral"></div>
  <div class="art" style="left:300px;top:90px;width:52px;height:66px" role="img" aria-label="Crane fund badge artwork"></div>
  <p class="para abs" style="left:362px;top:92px;width:180px;font-size:6.3px;text-align:center"><b style="color:var(--red)">Royal Crane Funds:</b> for investors who had always dreams of owning a restaurant or bar but want to avoid the high risk and want to participate in a highly liquid business</p>
  <p class="para abs" style="left:30px;top:196px;width:150px;font-size:6.3px;text-align:center"><b style="color:var(--red)">Deep Tide Funds:</b> for investors that appreciate "brick and mortar" investments, lower risk, income and with a longer exit horizon</p>
  <div class="abs" style="left:192px;top:210px;font-family:'Roboto Condensed',sans-serif;font-weight:700;font-size:7px;color:var(--red);letter-spacing:.5px">DEEP TIDE</div>
  <div class="abs" style="left:278px;top:176px;width:278px;height:98px;background:var(--coral);display:flex;align-items:flex-end;justify-content:center;padding-bottom:14px">
    <span style="font-family:'Roboto Condensed',sans-serif;font-weight:700;font-size:20px;color:#3a2b2b;letter-spacing:2px">DEEP TIDE CAPITAL</span>
  </div>
  <div class="foot"><b>Royal Crane Pitch Presentation</b> &nbsp;&nbsp; Page 02</div>
</section>

<section class="slide col-r" style="top:642px">
  <div class="art" style="left:34px;top:11px;width:213px;height:290px;border:4px solid var(--coral)" role="img" aria-label="Crowned crane brand artwork"></div>
  <div class="brand"><i></i>DEEP TIDE</div>
  <div class="abs" style="left:292px;top:40px;font-family:'Roboto Condensed',sans-serif;font-size:16px;color:var(--coral)">ROYAL CRANE</div>
  <div class="abs" style="left:292px;top:60px;font-size:4.5px;color:var(--grey)">LOREM IPSUM, GIVING INFORMATION ON ITS ORIGINS</div>
  <div class="para abs" style="left:292px;top:84px;width:235px;font-size:6.2px">
    <p>Royal Crane is a family of funds targeting the entertainment business. The business model of the funds is to acquire relevant brands in the food and entertainment industry looking for capital to expand their footprint.</p>
    <p style="margin-top:7px">We are focused on concepts that are curated, well managed, fit for their markets and scalable.</p>
    <p style="margin-top:7px">We intend to diversify away the high risk of investing in an entertainment venture</p>
    <p style="margin-top:7px">(with the associated statistics of failure) by buying into different concepts in different areas of the business in different geographies.</p>
  </div>
  <div class="foot"><b>Royal Crane Pitch Presentation</b> &nbsp;&nbsp; Page 03</div>
</section>

<!-- ROW 2 -->
<section class="slide col-l" style="top:965px">
  <div class="brand"><i></i>DEEP TIDE</div>
  <div class="s-title" style="top:34px">We identified and curated 6 concepts,...</div>
  <div class="s-sub" style="top:56px">Each following the objectives of the funds</div>
  <div class="art" style="left:44px;top:85px;width:198px;height:96px" role="img" aria-label="Sushi concept photo"></div><span class="cap" style="left:60px;top:170px">Tidewater Roll House</span>
  <div class="art muted" style="left:253px;top:85px;width:119px;height:96px" role="img" aria-label="Brewery concept photo"></div><span class="cap" style="left:262px;top:170px">Copperfield Brewing</span>
  <div class="art muted" style="left:384px;top:85px;width:122px;height:96px" role="img" aria-label="Poke concept photo"></div><span class="cap" style="left:394px;top:170px">Bright Bowl Poke</span>
  <div class="art muted" style="left:44px;top:186px;width:111px;height:82px" role="img" aria-label="Sake bar concept photo"></div><span class="cap" style="left:52px;top:258px">Lumen Sake Hall</span>
  <div class="art" style="left:168px;top:186px;width:204px;height:82px;background:linear-gradient(160deg,#f2f2f2,#dedede)" role="img" aria-label="Restaurant concept photo"></div><span class="cap" style="left:178px;top:258px;color:#777">Brasa Norte</span>
  <div class="art muted" style="left:384px;top:186px;width:122px;height:82px" role="img" aria-label="Entertainment venue concept photo"></div><span class="cap" style="left:390px;top:258px">Lantern Social Club</span>
  <div class="foot"><b>Royal Crane Pitch Presentation</b> &nbsp;&nbsp; Page 04</div>
</section>

<section class="slide col-r" style="top:965px">
  <div class="brand" style="left:30px;right:auto"><i></i>DEEP TIDE</div>
  <div class="abs" style="left:31px;top:58px;font-family:'Roboto Condensed',sans-serif;font-size:16px;color:var(--red)">THE PROJECT</div>
  <div class="para abs" style="left:31px;top:78px;width:196px;font-size:5.8px;line-height:1.4">
    <p>The project is expected to raise US$50M in its 2 associated funds:</p>
    <p style="margin-top:8px">- Reg. A: for public investors (to be registered in the Securities Exchange Commission) and available for small investors in the US</p>
    <p>- Reg. D: for private accredited investors in the US and internationally</p>
    <p style="margin-top:6px">Our target return for the combined project is 18%</p>
    <p>- We have curated the 6 brands targeted in this offering and risk-adjusted the returns based on the maturity of the concept, geographic diversity, current and future commitments and many other factors used for the underwriting of the project.</p>
    <p>- Details of expected return by project can be found in the schedule attached</p>
  </div>
  <div class="art" style="left:255px;top:0;width:120px;height:160px" role="img" aria-label="Crane artwork collage"></div>
  <div class="art" style="left:378px;top:0;width:178px;height:100px;background:linear-gradient(160deg,#fff,#f3f3f3);border:3px solid var(--coral)" role="img" aria-label="Crane artwork collage"></div>
  <div class="art" style="left:378px;top:104px;width:178px;height:120px" role="img" aria-label="Crane artwork collage"></div>
  <div class="art" style="left:255px;top:164px;width:120px;height:148px;background:linear-gradient(160deg,#fff,#f3f3f3);border:3px solid var(--coral)" role="img" aria-label="Crane artwork collage"></div>
  <div class="art" style="left:378px;top:228px;width:178px;height:84px" role="img" aria-label="Crane artwork collage"></div>
  <div class="foot"><b>Royal Crane Pitch Presentation</b> &nbsp;&nbsp; Page 05</div>
</section>

<!-- ROW 3 -->
<section class="slide col-l" style="top:1289px">
  <div class="brand"><i></i>DEEP TIDE</div>
  <div class="s-title" style="top:18px">Your title here</div>
  <div class="abs" style="left:41px;top:66px;width:474px">
    <table class="t-brand">
      <tr><th style="background:#fff;border:none"></th><th>Brand</th><th>Geography</th><th>Current # Stores</th><th>Future Stores</th><th>Management Team</th><th>Revenue Stream</th></tr>
      <tr><td class="nm">Tidewater Roll House</td><td>Established - Mature</td><td>Miami, Aventura, FLL</td><td>6</td><td>3</td><td>Established - Proven</td><td>Mature - Stable</td></tr>
      <tr><td class="nm">Copperfield Brewing</td><td>Established</td><td>Miami, FLL</td><td>2</td><td>2</td><td>Established - Developing</td><td>Growth</td></tr>
      <tr><td class="nm">Lumen Sake Hall</td><td>Developing</td><td>Miami, DC, Chicago, Austin, NYC, LA</td><td>1</td><td>6</td><td>Established - Developing</td><td>Developing</td></tr>
      <tr><td class="nm">Brasa Norte</td><td>Established</td><td>Argentina, Miami</td><td>2</td><td>4</td><td>Developing</td><td>Initiating</td></tr>
      <tr><td class="nm">Bright Bowl Poke</td><td>Initiating</td><td>Miami</td><td>1</td><td>7</td><td>Initiating</td><td>Initiating</td></tr>
      <tr><td class="nm">Lantern Social Club</td><td>Initiating</td><td>Mexico, Miami</td><td>1</td><td>1</td><td>Initiating</td><td>Initiating</td></tr>
    </table>
  </div>
  <div class="foot"><b>Royal Crane Pitch Presentation</b> &nbsp;&nbsp; Page 06</div>
</section>

<section class="slide col-r" style="top:1289px">
  <div class="brand"><i></i>DEEP TIDE</div>
  <div class="s-title" style="top:36px">Tabla master</div>
  <div class="s-sub" style="top:58px">Lorem ipsum, giving information on its origins, as well as a random text here</div>
  <div class="abs" style="left:46px;top:91px;font-size:5.5px">Finanzas (billions)</div>
  <div class="abs" style="left:46px;top:106px;width:472px">
    <table class="t-fin">
      <tr><th style="background:#fff"></th><th>2010</th><th>2011</th><th>2012</th><th>2013</th><th>2014</th><th>2015</th></tr>
      <tr><td>Gross Income</td><td>15.6</td><td>17.1</td><td>10.6</td><td>17.1</td><td>15.6</td><td>17.1</td></tr>
      <tr><td>Market Cost</td><td>10.6</td><td>10.8</td><td>10.6</td><td>10.8</td><td>10.6</td><td>10.8</td></tr>
      <tr><td>Ganancias Gruesas</td><td>5.0</td><td>6.3</td><td>5.0</td><td>6.3</td><td>5.0</td><td>6.3</td></tr>
      <tr><td>R&amp;D</td><td>0.48</td><td>0.49</td><td>0.48</td><td>0.49</td><td>0.48</td><td>0.49</td></tr>
      <tr><td>Total Sales</td><td>1.1</td><td>1.0</td><td>1.1</td><td>1.0</td><td>1.1</td><td>1.0</td></tr>
      <tr><td>Debts</td><td>3.4</td><td>4.8</td><td>3.4</td><td>4.8</td><td>3.4</td><td>4.8</td></tr>
      <tr><td>Taxes</td><td>1.3</td><td>1.9</td><td>1.3</td><td>1.9</td><td>1.3</td><td>1.9</td></tr>
      <tr><td>Bank</td><td>-</td><td>-</td><td>-</td><td>-</td><td>-</td><td>-</td></tr>
      <tr class="net"><td>Ingresos Netos</td><td>2.1</td><td>2.9</td><td>2.1</td><td>2.9</td><td>2.1</td><td>2.9</td></tr>
    </table>
  </div>
  <div class="foot"><b>Royal Crane Pitch Presentation</b> &nbsp;&nbsp; Page 07</div>
</section>

<!-- ROW 4 -->
<section class="slide col-l" style="top:1612px">
  <div class="brand"><i></i>DEEP TIDE</div>
  <div class="s-title" style="top:36px">Gráfico de barras</div>
  <div class="s-sub" style="top:58px">Lorem ipsum, giving information on its origins, as well as a random text here</div>
  <svg class="abs" style="left:30px;top:100px" width="230" height="170" viewBox="0 0 220 160" font-family="Roboto" font-size="6" fill="#444">
    <g stroke="#999" stroke-width=".6"><line x1="20" y1="10" x2="20" y2="140"/><line x1="20" y1="140" x2="215" y2="140"/></g>
    <g text-anchor="end"><text x="15" y="142">0</text><text x="15" y="116">2</text><text x="15" y="90">4</text><text x="15" y="64">6</text><text x="15" y="38">8</text><text x="15" y="12">10</text></g>
    <g fill="#e6312b"><rect x="28" y="80.2" width="18" height="59.8"/><rect x="60" y="82.8" width="18" height="57.2"/><rect x="92" y="68.5" width="18" height="71.5"/><rect x="124" y="46.4" width="18" height="93.6"/><rect x="156" y="34.7" width="18" height="105.3"/><rect x="188" y="21.7" width="18" height="118.3"/></g>
    <g fill="#fff" text-anchor="middle"><text x="37" y="88">4.6</text><text x="69" y="91">4.4</text><text x="101" y="76">5.5</text><text x="133" y="54">7.2</text><text x="165" y="42">8.1</text><text x="197" y="29">9.1</text></g>
    <g text-anchor="middle"><text x="37" y="152">2010</text><text x="69" y="152">2011</text><text x="101" y="152">2012</text><text x="133" y="152">2013</text><text x="165" y="152">2014</text><text x="197" y="152">2015</text></g>
  </svg>
  <svg class="abs" style="left:298px;top:100px" width="230" height="170" viewBox="0 0 220 160" font-family="Roboto" font-size="6" fill="#444">
    <g stroke="#999" stroke-width=".6"><line x1="20" y1="10" x2="20" y2="140"/><line x1="20" y1="140" x2="215" y2="140"/></g>
    <g text-anchor="end"><text x="15" y="142">0</text><text x="15" y="116">2</text><text x="15" y="90">4</text><text x="15" y="64">6</text><text x="15" y="38">8</text><text x="15" y="12">10</text></g>
    <rect x="28" y="80.2" width="18" height="59.8" fill="#e6312b"/><rect x="60" y="82.8" width="18" height="57.2" fill="#e6312b"/><rect x="92" y="68.5" width="18" height="71.5" fill="#c0201e"/><rect x="124" y="46.4" width="18" height="93.6" fill="#b31a19"/><rect x="156" y="34.7" width="18" height="105.3" fill="#9c1212"/><rect x="188" y="21.7" width="18" height="118.3" fill="#8a0f0f"/>
    <g fill="#fff" text-anchor="middle"><text x="37" y="88">4.6</text><text x="69" y="91">4.4</text><text x="101" y="76">5.5</text><text x="133" y="54">7.2</text><text x="165" y="42">8.1</text><text x="197" y="29">9.1</text></g>
    <g text-anchor="middle"><text x="37" y="152">2010</text><text x="69" y="152">2011</text><text x="101" y="152">2012</text><text x="133" y="152">2013</text><text x="165" y="152">2014</text><text x="197" y="152">2015</text></g>
  </svg>
  <div class="foot"><b>Royal Crane Pitch Presentation</b> &nbsp;&nbsp; Page 08</div>
</section>

<section class="slide col-r" style="top:1612px">
  <div class="abs" style="left:42px;top:36px;font-family:'Roboto Condensed',sans-serif;font-size:16px;color:var(--coral)">DEEP TIDE CAPITAL</div>
  <div class="abs" style="left:42px;top:56px;font-size:4.5px;color:var(--grey)">LOREM IPSUM, GIVING INFORMATION ON ITS ORIGINS, AS WELL AS A RANDOM TEXT HERE</div>
  <div class="para abs" style="left:42px;top:74px;width:250px;font-size:5.7px;font-weight:700;line-height:1.35;text-align:justify;color:#333">
    <p>Deep Tide Capital is a family of funds targeting the real estate business. The business model of the funds is to acquire income producing properties or projects for development to derive a steady income.</p>
    <p style="margin-top:5px">We underwrite projects based on their own merits focused on achieving the fund goal.</p>
    <p style="margin-top:5px">The properties are well managed, preferably environmentally friendly, trendy in their markets and value at the right point.</p>
    <p style="margin-top:5px">We intend to diversify away the high risk of investing in one property by combining several properties (from different industries (hospitality, entertainment, retail, residential, etc.)</p>
    <p style="margin-top:5px">The exit side of our business model is predicated on the increased value of the property once it has been developed. We take advantage of opportunistic sales of our portfolio and design an exit strategy before investing.</p>
  </div>
  <div class="abs" style="left:300px;top:135px;white-space:nowrap;font-family:'Roboto Condensed',sans-serif;font-weight:700;font-size:44px;color:var(--coral);letter-spacing:1px">DEEP TIDE</div>
  <div class="abs" style="left:306px;top:190px;white-space:nowrap;font-family:'Roboto Condensed',sans-serif;font-size:20px;color:#f4a09b;letter-spacing:1px">A New Generation Of Investors</div>
  <div class="foot"><b>Royal Crane Pitch Presentation</b> &nbsp;&nbsp; Page 09</div>
</section>

<!-- ROW 5 -->
<section class="slide col-l" style="top:1936px">
  <div class="brand"><i></i>DEEP TIDE</div>
  <div class="s-title left" style="top:20px;font-size:16px;color:var(--red)">We identified 6 properties for investment</div>
  <div class="photo" style="left:24px;top:70px;width:122px;height:101px" role="img" aria-label="Property photo"></div>
  <div class="abs" style="left:151px;top:70px;width:122px;height:101px;background:var(--red);opacity:.92;color:#fff;padding:26px 8px 0 10px">
    <div style="font-family:'Roboto Condensed',sans-serif;font-weight:700;font-size:7.5px;line-height:1.1">ABOUT THE<br>PROJECT</div>
    <p style="font-size:4.8px;line-height:1.35;margin-top:4px">Lorem ipsum dolor sit amet, consectetuer adipiscing elit. Maecenas porttitor congue massa. Fusce posuere, magna sed pulvinar ultricies.</p>
  </div>
  <div class="photo" style="left:282px;top:70px;width:122px;height:101px" role="img" aria-label="Property photo"></div>
  <div class="photo" style="left:409px;top:70px;width:122px;height:101px" role="img" aria-label="Property photo"></div>
  <div class="photo" style="left:24px;top:177px;width:122px;height:101px" role="img" aria-label="Property photo"></div>
  <div class="photo" style="left:151px;top:177px;width:122px;height:101px" role="img" aria-label="Property photo"></div>
  <div class="photo" style="left:282px;top:177px;width:122px;height:101px" role="img" aria-label="Property photo"></div>
  <div class="abs" style="left:409px;top:177px;width:122px;height:101px;background:var(--red);color:#fff;padding:20px 8px 0 10px">
    <div style="font-family:'Roboto Condensed',sans-serif;font-weight:700;font-size:7.5px;line-height:1.1">ABOUT THE<br>PROJECT</div>
    <p style="font-size:4.8px;line-height:1.35;margin-top:4px">Lorem ipsum dolor sit amet, consectetuer adipiscing elit. Maecenas porttitor congue massa. Fusce posuere, magna sed pulvinar ultricies.</p>
  </div>
  <div class="foot"><b>Royal Crane Pitch Presentation</b> &nbsp;&nbsp; Page 10</div>
</section>

<section class="slide col-r" style="top:1936px">
  <div class="brand"><i></i>DEEP TIDE</div>
  <div class="s-title" style="top:38px">Bar graphics</div>
  <div class="s-sub" style="top:60px">Lorem ipsum, giving information on its origins, as well as a random text here</div>
  <div class="para abs" style="left:50px;top:96px;width:180px;font-size:7px;line-height:1.3;color:#333">
    <p>Lorem ipsum dolor sit amet, consectetuer adipiscing elit. Maecenas porttitor congue massa. Fusce posuere, magna sed pulvinar ultricies.</p>
    <p style="margin-top:10px">Lorem ipsum dolor sit amet, consectetuer adipiscing elit. Maecenas porttitor congue massa. Fusce posuere, magna sed pulvinar ultricies.</p>
    <p style="margin-top:10px">Lorem ipsum dolor sit amet, consectetuer adipiscing elit. Maecenas porttitor congue massa. Fusce posuere, magna sed pulvinar ultricies.</p>
  </div>
  <svg class="abs" style="left:280px;top:100px" width="240" height="175" viewBox="0 0 220 160" font-family="Roboto" font-size="6" fill="#444">
    <g stroke="#999" stroke-width=".6"><line x1="20" y1="10" x2="20" y2="140"/><line x1="20" y1="140" x2="215" y2="140"/></g>
    <g text-anchor="end"><text x="15" y="142">0</text><text x="15" y="116">2</text><text x="15" y="90">4</text><text x="15" y="64">6</text><text x="15" y="38">8</text><text x="15" y="12">10</text></g>
    <rect x="28" y="80.2" width="18" height="59.8" fill="#f0655f"/><rect x="60" y="82.8" width="18" height="57.2" fill="#e6312b"/><rect x="92" y="68.5" width="18" height="71.5" fill="#d42622"/><rect x="124" y="46.4" width="18" height="93.6" fill="#c0201e"/><rect x="156" y="34.7" width="18" height="105.3" fill="#9c1212"/><rect x="188" y="21.7" width="18" height="118.3" fill="#7d0d0d"/>
    <g fill="#fff" text-anchor="middle"><text x="37" y="88">4.6</text><text x="69" y="91">4.4</text><text x="101" y="76">5.5</text><text x="133" y="54">7.2</text><text x="165" y="42">8.1</text><text x="197" y="29">9.1</text></g>
    <g text-anchor="middle"><text x="37" y="152">2010</text><text x="69" y="152">2011</text><text x="101" y="152">2012</text><text x="133" y="152">2013</text><text x="165" y="152">2014</text><text x="197" y="152">2015</text></g>
  </svg>
  <div class="foot"><b>Royal Crane Pitch Presentation</b> &nbsp;&nbsp; Page 11</div>
</section>

<!-- ROW 6 -->
<section class="slide col-l" style="top:2259px">
  <div class="brand"><i></i>DEEP TIDE</div>
  <div class="s-title" style="top:36px">Line grafico</div>
  <div class="s-sub" style="top:58px">Lorem ipsum, giving information on its origins, as well as a random text here</div>
  <svg class="abs" style="left:24px;top:84px" width="510" height="190" viewBox="0 0 510 190" font-family="Roboto" font-size="6" fill="#444">
    <g stroke="#e3e3e3" stroke-width=".6">
      <line x1="30" y1="10" x2="500" y2="10"/><line x1="30" y1="25" x2="500" y2="25"/><line x1="30" y1="40" x2="500" y2="40"/><line x1="30" y1="55" x2="500" y2="55"/><line x1="30" y1="70" x2="500" y2="70"/><line x1="30" y1="85" x2="500" y2="85"/><line x1="30" y1="100" x2="500" y2="100"/><line x1="30" y1="115" x2="500" y2="115"/><line x1="30" y1="130" x2="500" y2="130"/><line x1="30" y1="145" x2="500" y2="145"/>
    </g>
    <line x1="30" y1="160" x2="500" y2="160" stroke="#999" stroke-width=".6"/>
    <g text-anchor="end"><text x="24" y="12">50</text><text x="24" y="27">45</text><text x="24" y="42">40</text><text x="24" y="57">35</text><text x="24" y="72">30</text><text x="24" y="87">25</text><text x="24" y="102">20</text><text x="24" y="117">15</text><text x="24" y="132">10</text><text x="24" y="147">5</text><text x="24" y="162">0</text></g>
    <g text-anchor="middle"><text x="30" y="174">4/14/02</text><text x="90" y="174">5/4/02</text><text x="150" y="174">5/24/02</text><text x="210" y="174">6/13/02</text><text x="270" y="174">7/3/02</text><text x="330" y="174">7/23/02</text><text x="390" y="174">8/12/02</text><text x="450" y="174">9/1/02</text><text x="500" y="174">9/21/02</text></g>
    <g fill="none" stroke-width="1.3">
      <path d="M90 95 C140 60 180 30 220 55 S290 90 300 98 S380 90 430 82" stroke="#e6312b"/>
      <path d="M90 88 C160 95 220 100 300 110 S390 95 430 88" stroke="#f0655f"/>
      <path d="M90 112 C150 120 220 130 280 122 S380 100 430 98" stroke="#9c1212"/>
    </g>
  </svg>
  <div class="foot"><b>Royal Crane Pitch Presentation</b> &nbsp;&nbsp; Page 12</div>
</section>

<section class="slide col-r" style="top:2259px;background:linear-gradient(180deg,#c7c7c7,#a9a9a9)">
  <div class="abs" style="left:48px;top:150px;width:70px;height:1px;background:#fff"></div>
  <div class="abs" style="left:438px;top:150px;width:70px;height:1px;background:#fff"></div>
  <div class="abs" style="left:0;right:0;top:138px;text-align:center;font-family:'Roboto Condensed',sans-serif;font-weight:700;font-size:24px;letter-spacing:2px;color:#fff">YOUR <span style="color:var(--coral)">PRESENTACIÓN</span></div>
  <div class="abs" style="left:0;right:0;top:168px;text-align:center;font-size:4.5px;letter-spacing:1px;color:#eee">BUSINESS PRESENTATION TEMPLATE</div>
  <div class="abs" style="left:-10px;right:-10px;top:178px;text-align:center;font-family:'Roboto Condensed',sans-serif;font-weight:700;font-size:46px;letter-spacing:3px;color:#3f3f3f">DEEP TIDE CAPITAL</div>
  <div class="abs" style="left:0;right:0;top:238px;text-align:center;font-size:20px;color:#8b8b8b;letter-spacing:.5px">A New Generation Of Investors.</div>
</section>

<!-- ROW 7 -->
<section class="slide col-l" style="top:2583px">
  <div class="brand"><i></i>DEEP TIDE</div>
  <div class="s-title" style="top:36px">Top 3 benefits</div>
  <div class="s-sub" style="top:58px">Lorem ipsum, giving information on its origins, as well as a random text here</div>
  <div class="benefit" style="top:86px">
    <svg width="24" height="20" viewBox="0 0 24 20"><path d="M2 10 L9 17 L22 3" fill="none" stroke="#e6312b" stroke-width="4"/></svg>
    <div><h4>360 &nbsp;Free Support.</h4><p>Lorem ipsum is simply dummy text of the printing and typesetting industry. Lorem ipsum has been the industry's standard dummy text ever.</p></div>
  </div>
  <div class="benefit" style="top:146px">
    <svg width="24" height="20" viewBox="0 0 24 20"><path d="M2 10 L9 17 L22 3" fill="none" stroke="#e6312b" stroke-width="4"/></svg>
    <div><h4>$3600 with &nbsp;year Suscription</h4><p>Lorem ipsum is simply dummy text of the printing and typesetting industry. Lorem ipsum has been the industry's standard dummy text ever.</p></div>
  </div>
  <div class="benefit" style="top:206px">
    <svg width="24" height="20" viewBox="0 0 24 20"><path d="M2 10 L9 17 L22 3" fill="none" stroke="#e6312b" stroke-width="4"/></svg>
    <div><h4>24/7 Support</h4><p>Lorem ipsum is simply dummy text of the printing and typesetting industry. Lorem ipsum has been the industry's standard dummy text ever.</p></div>
  </div>
  <div class="foot"><b>Royal Crane Pitch Presentation</b> &nbsp;&nbsp; Page 14</div>
</section>

<section class="slide col-r" style="top:2583px">
  <div class="s-title left" style="top:36px;left:42px">Our competitors</div>
  <div class="abs" style="left:42px;top:58px;font-size:4.5px;color:var(--grey)">LOREM IPSUM, GIVING INFORMATION ON ITS ORIGINS, AS WELL AS A RANDOM TEXT HERE</div>
  <div class="circ" style="left:60px;top:98px"><i style="width:34px;height:34px;border-radius:4px;background:var(--red)"></i><div><h4 style="font-size:8px">NAME</h4><p>Lorem ipsum is simply dummy text of the printing and typesetting.</p></div></div>
  <div class="circ" style="left:60px;top:156px"><i style="width:34px;height:34px;border-radius:4px;background:var(--deep)"></i><div><h4 style="font-size:8px">TNAME</h4><p>Lorem ipsum is simply dummy text of the printing and typesetting.</p></div></div>
  <div class="circ" style="left:60px;top:214px"><i style="width:34px;height:34px;border-radius:4px;background:var(--red)"></i><div><h4 style="font-size:8px">Name</h4><p>Lorem ipsum is simply dummy text of the printing and typesetting.</p></div></div>
  <svg class="abs" style="left:0;top:0" width="556" height="312" viewBox="0 0 556 312">
    <defs><linearGradient id="compFill" x1="0" y1="0" x2="1" y2="1"><stop offset="0" stop-color="#f4827c"/><stop offset="1" stop-color="#e9544d"/></linearGradient></defs>
    <polygon role="img" aria-label="Crowned crane brand artwork" points="330,312 372,0 556,0 556,312" fill="url(#compFill)"/>
    <line x1="300" y1="312" x2="344" y2="0" stroke="#f0655f" stroke-width="1"/>
    <line x1="520" y1="312" x2="556" y2="60" stroke="#fff" stroke-width="6"/>
  </svg>
  <div class="foot"><b>Royal Crane Pitch Presentation</b> &nbsp;&nbsp; Page 15</div>
</section>

<!-- ROW 8 -->
<section class="slide col-l" style="top:2906px">
  <div class="brand"><i></i>DEEP TIDE</div>
  <div class="s-title left plain" style="top:22px;font-size:15px;color:var(--red)">Project benefits</div>
  <div class="abs" style="left:140px;top:42px;width:150px;height:1px;background:var(--coral)"></div>
  <div class="photo" style="left:24px;top:85px;width:246px;height:188px;background:linear-gradient(135deg,#e4e4e4,#d2d2d2)" role="img" aria-label="Project photo"></div>
  <svg class="abs" style="left:24px;top:221px" width="70" height="52"><polygon points="0,0 70,52 0,52" fill="#e6312b"/></svg>
  <svg class="abs" style="left:514px;top:86px" width="20" height="16"><polygon points="0,0 20,0 20,16" fill="#e6312b"/></svg>
  <div class="ticks" style="left:294px;top:88px">
    <div class="tick"><span class="dot"><svg width="8" height="7"><path d="M1 3.5 L3.3 6 L7 1" stroke="#fff" stroke-width="1.6" fill="none"/></svg></span><div><h4>WE MANAGE</h4><p>Simply dummy text of the printing and typesetting industry, standard dummy.</p></div></div>
    <div class="tick"><span class="dot"><svg width="8" height="7"><path d="M1 3.5 L3.3 6 L7 1" stroke="#fff" stroke-width="1.6" fill="none"/></svg></span><div><h4>WE INSPIRE</h4><p>Simply dummy text of the printing and typesetting industry, standard dummy.</p></div></div>
    <div class="tick"><span class="dot"><svg width="8" height="7"><path d="M1 3.5 L3.3 6 L7 1" stroke="#fff" stroke-width="1.6" fill="none"/></svg></span><div><h4>WE SEARCH</h4><p>Simply dummy text of the printing and typesetting industry, standard dummy.</p></div></div>
    <div class="tick"><span class="dot"><svg width="8" height="7"><path d="M1 3.5 L3.3 6 L7 1" stroke="#fff" stroke-width="1.6" fill="none"/></svg></span><div><h4>WE CREATE</h4><p>Simply dummy text of the printing and typesetting industry, standard dummy.</p></div></div>
    <div class="tick"><span class="dot"><svg width="8" height="7"><path d="M1 3.5 L3.3 6 L7 1" stroke="#fff" stroke-width="1.6" fill="none"/></svg></span><div><h4>WE CREATE</h4><p>Simply dummy text of the printing and typesetting industry, standard dummy.</p></div></div>
  </div>
  <div class="foot"><b>Royal Crane Pitch Presentation</b> &nbsp;&nbsp; Page 16</div>
</section>

<section class="slide col-r" style="top:2906px">
  <div class="brand"><i></i></div>
  <div class="s-title left" style="top:20px;font-size:15px;color:var(--red)">Solution adventage</div>
  <div class="abs" style="left:30px;top:40px;width:150px;height:1px;background:var(--coral)"></div>
  <div class="ticks" style="left:26px;top:82px">
    <div class="tick"><span class="dot"><svg width="8" height="7"><path d="M1 3.5 L3.3 6 L7 1" stroke="#fff" stroke-width="1.6" fill="none"/></svg></span><div><h4>WE MANAGE</h4><p>Simply dummy text of the printing and typesetting industry, standard dummy.</p></div></div>
    <div class="tick"><span class="dot"><svg width="8" height="7"><path d="M1 3.5 L3.3 6 L7 1" stroke="#fff" stroke-width="1.6" fill="none"/></svg></span><div><h4>WE INSPIRE</h4><p>Simply dummy text of the printing and typesetting industry, standard dummy.</p></div></div>
    <div class="tick"><span class="dot"><svg width="8" height="7"><path d="M1 3.5 L3.3 6 L7 1" stroke="#fff" stroke-width="1.6" fill="none"/></svg></span><div><h4>WE SEARCH</h4><p>Simply dummy text of the printing and typesetting industry, standard dummy.</p></div></div>
    <div class="tick"><span class="dot"><svg width="8" height="7"><path d="M1 3.5 L3.3 6 L7 1" stroke="#fff" stroke-width="1.6" fill="none"/></svg></span><div><h4>WE CREATE</h4><p>Simply dummy text of the printing and typesetting industry, standard dummy.</p></div></div>
    <div class="tick"><span class="dot"><svg width="8" height="7"><path d="M1 3.5 L3.3 6 L7 1" stroke="#fff" stroke-width="1.6" fill="none"/></svg></span><div><h4>WE CREATE</h4><p>Simply dummy text of the printing and typesetting industry, standard dummy.</p></div></div>
  </div>
  <div class="photo" style="left:278px;top:82px;width:254px;height:190px;background:linear-gradient(135deg,#e4e4e4,#d2d2d2)" role="img" aria-label="Solution photo"></div>
  <svg class="abs" style="left:462px;top:220px" width="70" height="52"><polygon points="70,0 70,52 0,52" fill="#e6312b"/></svg>
  <div class="foot"><b>Royal Crane Pitch Presentation</b> &nbsp;&nbsp; Page 17</div>
</section>

<!-- ROW 9 -->
<section class="slide col-l" style="top:3230px">
  <div class="brand"><i></i>DEEP TIDE</div>
  <div class="s-title" style="top:36px">Solution adventage</div>
  <div class="s-sub" style="top:58px">Lorem ipsum, giving information on its origins, as well as a random text here</div>
  <div class="circ" style="left:64px;top:92px"><i style="background:var(--red)"></i><div><h4>Sinergies</h4><p>Ea ria qui del sum aut ece et estrum nonsequia volupta doluptas illuptas</p></div></div>
  <div class="circ" style="left:286px;top:92px"><i style="background:var(--red)"></i><div><h4>Network</h4><p>Ea ria qui del sum aut ece et estrum nonsequia volupta doluptas illuptas</p></div></div>
  <div class="circ" style="left:64px;top:152px"><i style="background:#c0201e"></i><div><h4>Financial Aventaje</h4><p>Ea ria qui del sum aut ece et estrum nonsequia volupta doluptas illuptas</p></div></div>
  <div class="circ" style="left:286px;top:152px"><i style="background:var(--deep)"></i><div><h4>Experience Team</h4><p>Ea ria qui del sum aut ece et estrum nonsequia volupta doluptas illuptas</p></div></div>
  <div class="circ" style="left:64px;top:212px"><i style="background:var(--darkest)"></i><div><h4>Global Service</h4><p>Ea ria qui del sum aut ece et estrum nonsequia volupta doluptas illuptas</p></div></div>
  <div class="circ" style="left:286px;top:212px"><i style="background:#c0201e"></i><div><h4>Manufacture</h4><p>Ea ria qui del sum aut ece et estrum nonsequia volupta doluptas illuptas</p></div></div>
  <div class="foot"><b>Royal Crane Pitch Presentation</b> &nbsp;&nbsp; Page 18</div>
</section>

<section class="slide col-r" style="top:3230px">
  <div class="brand"><i></i>DEEP TIDE</div>
  <div class="s-title" style="top:36px;color:var(--red)">We have identified 6 properties for investment:</div>
  <div class="s-sub" style="top:58px">Lorem ipsum, giving information on its origins, as well as a random text here</div>
  <div class="photo" style="left:23px;top:88px;width:82px;height:82px" role="img" aria-label="Airport inn photo"></div>
  <div class="photo" style="left:108px;top:88px;width:82px;height:82px" role="img" aria-label="Tower photo"></div>
  <div class="photo" style="left:193px;top:88px;width:82px;height:82px" role="img" aria-label="Hotel photo"></div>
  <div class="photo" style="left:278px;top:88px;width:82px;height:82px" role="img" aria-label="Courtyard photo"></div>
  <div class="photo" style="left:363px;top:88px;width:82px;height:82px" role="img" aria-label="Historic building photo"></div>
  <div class="photo" style="left:448px;top:88px;width:82px;height:82px" role="img" aria-label="Sixth property photo"></div>
  <div class="abs" style="left:23px;top:176px;width:507px;display:grid;grid-template-columns:repeat(6,82px);column-gap:3px;font-size:6.5px;text-align:center;color:#222">
    <span>Gateway Field Inn</span><span>Beacon Point Tower</span><span>The Linden Stay</span><span>The Fern Courtyard</span><span>The Signal House</span><span>6th Property</span>
  </div>
  <div class="abs" style="left:23px;top:196px;width:507px;display:grid;grid-template-columns:repeat(6,82px);column-gap:3px;font-size:4.8px;line-height:1.35;color:#666">
    <span><b>Lorem ipsum</b> is simply dummy text of the printing and typesetting industry</span><span><b>Lorem ipsum</b> is simply dummy text of the printing and typesetting industry</span><span><b>Lorem ipsum</b> is simply dummy text of the printing and typesetting industry</span><span><b>Lorem ipsum</b> is simply dummy text of the printing and typesetting industry</span><span><b>Lorem ipsum</b> is simply dummy text of the printing and typesetting industry</span><span><b>Lorem ipsum</b> is simply dummy text of the printing and typesetting industry</span>
  </div>
  <div class="foot"><b>Royal Crane Pitch Presentation</b> &nbsp;&nbsp; Page 19</div>
</section>

<!-- ROW 10 -->
<section class="slide col-l" style="top:3553px">
  <div class="brand"><i></i>DEEP TIDE</div>
  <div class="abs" style="left:42px;top:30px;font-family:'Roboto Condensed',sans-serif;font-size:15px;color:#111">Timeline – 5 Years</div>
  <div class="abs" style="left:20px;top:179px;width:516px;height:2px;background:var(--red)"></div>
  <div class="tl-stem" style="left:97px;top:118px;height:62px"></div>
  <div class="tl-stem" style="left:298px;top:118px;height:62px"></div>
  <div class="tl-stem" style="left:500px;top:118px;height:62px"></div>
  <div class="tl-stem" style="left:200px;top:180px;height:62px"></div>
  <div class="tl-stem" style="left:401px;top:180px;height:62px"></div>
  <div class="tl-text" style="left:98px;top:94px"><b>Text Title</b>This is a sample text.<br>place your own text here</div>
  <div class="tl-text" style="left:299px;top:94px"><b>Text Title</b>This is a sample text.<br>place your own text here</div>
  <div class="tl-text" style="left:501px;top:94px"><b>Text Title</b>This is a sample text.<br>place your own text here</div>
  <div class="tl-text alt" style="left:201px;top:246px"><b>Text Title</b>This is a sample text.<br>place your own text here</div>
  <div class="tl-text alt" style="left:402px;top:246px"><b>Text Title</b>This is a sample text.<br>place your own text here</div>
  <div class="tl-node" style="left:98px;top:180px"><svg width="10" height="12"><rect x="1" y="1" width="8" height="10" fill="#fff"/></svg></div>
  <div class="tl-node" style="left:201px;top:180px"><svg width="12" height="12"><circle cx="6" cy="6" r="4" fill="none" stroke="#fff" stroke-width="2.5" stroke-dasharray="2 1.2"/></svg></div>
  <div class="tl-node" style="left:299px;top:180px"><svg width="13" height="10"><rect x="0" y="1" width="8" height="6" fill="#fff"/><rect x="8" y="3" width="4" height="4" fill="#fff"/><circle cx="3" cy="8" r="1.5" fill="#fff"/><circle cx="10" cy="8" r="1.5" fill="#fff"/></svg></div>
  <div class="tl-node" style="left:402px;top:180px"><svg width="11" height="12"><path d="M1 1 H10 V6 Q10 10 5.5 11.5 Q1 10 1 6 Z" fill="#fff"/></svg></div>
  <div class="tl-node" style="left:501px;top:180px"><svg width="11" height="12"><rect x="1" y="0" width="1.5" height="12" fill="#fff"/><path d="M2.5 1 H10 L8 3.5 L10 6 H2.5 Z" fill="#fff"/></svg></div>
  <div class="tl-year" style="left:98px;top:206px">2018</div>
  <div class="tl-year" style="left:201px;top:143px">2019</div>
  <div class="tl-year" style="left:299px;top:206px">2020</div>
  <div class="tl-year" style="left:402px;top:143px">2021</div>
  <div class="tl-year" style="left:501px;top:206px">2022</div>
  <div class="foot"><b>Royal Crane Pitch Presentation</b> &nbsp;&nbsp; Page 20</div>
</section>

<section class="slide col-r" style="top:3553px">
  <div class="brand"><i></i>DEEP TIDE</div>
  <div class="abs" style="left:36px;top:24px;font-family:'Roboto Condensed',sans-serif;font-size:15px;color:#111">Timeline – 4 Years</div>
  <div class="abs" style="left:66px;top:172px;width:424px;height:2px;background:var(--red)"></div>
  <div class="tl-stem" style="left:246px;top:110px;height:62px"></div>
  <div class="tl-stem" style="left:448px;top:110px;height:62px"></div>
  <div class="tl-stem" style="left:144px;top:173px;height:62px"></div>
  <div class="tl-stem" style="left:347px;top:173px;height:62px"></div>
  <div class="tl-text" style="left:247px;top:86px"><b>Text Title</b>This is a sample text.<br>place your own text here</div>
  <div class="tl-text" style="left:449px;top:86px"><b>Text Title</b>This is a sample text.<br>place your own text here</div>
  <div class="tl-text alt" style="left:145px;top:238px"><b>Text Title</b>This is a sample text.<br>place your own text here</div>
  <div class="tl-text alt" style="left:348px;top:238px"><b>Text Title</b>This is a sample text.<br>place your own text here</div>
  <div class="tl-node" style="left:145px;top:173px"><svg width="12" height="12"><circle cx="6" cy="6" r="4" fill="none" stroke="#fff" stroke-width="2.5" stroke-dasharray="2 1.2"/></svg></div>
  <div class="tl-node" style="left:247px;top:173px"><svg width="13" height="10"><rect x="0" y="1" width="8" height="6" fill="#fff"/><rect x="8" y="3" width="4" height="4" fill="#fff"/><circle cx="3" cy="8" r="1.5" fill="#fff"/><circle cx="10" cy="8" r="1.5" fill="#fff"/></svg></div>
  <div class="tl-node" style="left:348px;top:173px"><svg width="11" height="12"><path d="M1 1 H10 V6 Q10 10 5.5 11.5 Q1 10 1 6 Z" fill="#fff"/></svg></div>
  <div class="tl-node" style="left:449px;top:173px"><svg width="11" height="12"><rect x="1" y="0" width="1.5" height="12" fill="#fff"/><path d="M2.5 1 H10 L8 3.5 L10 6 H2.5 Z" fill="#fff"/></svg></div>
  <div class="tl-year" style="left:145px;top:136px">2018</div>
  <div class="tl-year" style="left:247px;top:198px">2019</div>
  <div class="tl-year" style="left:348px;top:136px">2020</div>
  <div class="tl-year" style="left:449px;top:198px">2021</div>
  <div class="foot"><b>Royal Crane Pitch Presentation</b> &nbsp;&nbsp; Page 21</div>
</section>

<!-- ROW 11 -->
<section class="slide col-l" style="top:3877px">
  <div class="brand"><i></i>DEEP TIDE</div>
  <div class="abs" style="left:42px;top:24px;font-family:'Roboto Condensed',sans-serif;font-size:14px;color:var(--red)">CALLOUT TIMELINE</div>
  <div class="abs" style="left:42px;top:44px;font-size:4.5px;color:#aaa">Simple vertical steps to share the plan</div>
  <div class="abs" style="left:143px;top:80px;width:2px;height:210px;background:#d4d4d4"></div>
  <div class="date" style="left:70px;top:98px">August<b>2019</b></div>
  <div class="vnode" style="left:144px;top:112px"></div>
  <div class="call red" style="left:176px;top:78px;width:314px;height:82px;padding-top:8px"><small>SUB DESCRIPTION</small><h4>Preparing Project Requirements</h4><p>The quick, brown fox jumps over a lazy dog. DJs flock by when TV ax quiz prog. Junk TV quiz graced by fox whelps.</p></div>
  <div class="date" style="left:70px;top:188px">October<b>2019</b></div>
  <div class="vnode" style="left:144px;top:202px"></div>
  <div class="call gray" style="left:176px;top:184px;width:314px;height:44px"><h4 style="font-size:9px">Starting Project</h4><p>The quick, brown fox jumps over a lazy dog. DJs flock by when TV ax quiz prog. Junk TV quiz graced by fox whelps.</p></div>
  <div class="date" style="left:70px;top:244px">January<b>2020</b></div>
  <div class="vnode" style="left:144px;top:258px"></div>
  <div class="call gray" style="left:176px;top:240px;width:314px;height:44px"><h4 style="font-size:9px">Middle Check</h4><p>The quick, brown fox jumps over a lazy dog. DJs flock by when TV ax quiz prog. Junk TV quiz graced by fox whelps.</p></div>
  <div class="foot"><b>Royal Crane Pitch Presentation</b> &nbsp;&nbsp; Page 22</div>
</section>

<section class="slide col-r" style="top:3877px">
  <div class="abs" style="left:143px;top:20px;width:2px;height:260px;background:#d4d4d4"></div>
  <div class="date" style="left:70px;top:26px">March<b>2020</b></div>
  <div class="vnode" style="left:144px;top:40px"></div>
  <div class="call gray" style="left:175px;top:20px;width:294px;height:44px"><h4 style="font-size:9px">Continue Project</h4><p>The quick, brown fox jumps over a lazy dog. DJs flock by when TV ax quiz prog. Junk TV quiz graced by fox whelps.</p></div>
  <div class="date" style="left:70px;top:84px">May<b>2020</b></div>
  <div class="vnode" style="left:144px;top:98px"></div>
  <div class="call gray" style="left:175px;top:78px;width:294px;height:44px"><h4 style="font-size:9px">Testing Section</h4><p>The quick, brown fox jumps over a lazy dog. DJs flock by when TV ax quiz prog. Junk TV quiz graced by fox whelps.</p></div>
  <div class="date" style="left:70px;top:142px">August<b>2020</b></div>
  <div class="vnode" style="left:144px;top:156px"></div>
  <div class="call gray" style="left:175px;top:136px;width:294px;height:44px"><h4 style="font-size:9px">Packaging Step</h4><p>The quick, brown fox jumps over a lazy dog. DJs flock by when TV ax quiz prog. Junk TV quiz graced by fox whelps.</p></div>
  <div class="date" style="left:70px;top:200px">October<b>2020</b></div>
  <div class="vnode" style="left:144px;top:214px"></div>
  <div class="call red" style="left:175px;top:194px;width:320px;height:66px"><small>SUB DESCRIPTION</small><h4>Finishing Project</h4><p>The quick, brown fox jumps over a lazy dog. DJs flock by when TV ax quiz prog. Junk TV quiz graced by fox whelps.</p></div>
</section>

</body>
</html>
```